KVT Calculator

We have a calculator already created however the design seems to be very boring and bland. The calculators goal is to show graphic designers, web development firms, pr agencies, marketing firms how much revenue they can potentially make by offering a managed social media solution to their clients.

We want a great designer to make the calculator appealing to our audience.

It is an amazing offer and opportunity however I do not believe the current design does it justice

you can view and play with calculator live at http://sandbox.plorvinix.com/qzta/

```html
<!DOCTYPE html>
<html lang="en">
<head>
<meta charset="utf-8">
<title>Revenue Calculator</title>
<link rel="stylesheet" href="https://fonts.googleapis.com/css2?family=Open+Sans:wght@400;600&display=swap">
<style>
  :root {
    --sky: #0a96f2;
    --panel: #333333;
    --white: #ffffff;
    --ink: #111111;
    --basic: #29a8e0;
    --pro: #f7931e;
    --enterprise: #39b54a;
    --tick: #6b0f0f;
    --mercury: #e0262b;
  }
  * { box-sizing: border-box; margin: 0; padding: 0; }
  html, body { width: 1200px; height: 800px; overflow: hidden; }
  body {
    background: var(--sky);
    font-family: "Open Sans", Arial, sans-serif;
    position: relative;
  }
  .calculator-panel {
    position: absolute; left: 82px; top: 208px; width: 1038px; height: 431px;
    background: var(--panel); border-bottom: 3px solid var(--white); border-radius: 3px;
  }
  .term-slider {
    position: absolute; left: 121px; top: 163px; width: 116px; height: 473px;
    border: 2px solid #1c1c1c; border-radius: 4px; overflow: hidden;
    background: linear-gradient(90deg, #8e8e8e 0%, #d8d8d8 22%, #f4f4f4 45%, #cfcfcf 70%, #8a8a8a 100%);
  }
  .term-slider__title {
    height: 44px; background: #2b2b2b; color: var(--white);
    font-size: 15px; font-weight: 600; letter-spacing: 1px; text-align: center; line-height: 44px;
  }
  .term-slider svg { position: absolute; left: 0; top: 0; }
  .field-label {
    position: absolute; left: 276px; color: var(--white);
    font-size: 15.5px; letter-spacing: 1.9px;
  }
  .label-rule { position: absolute; left: 276px; width: 221px; height: 1px; background: var(--white); }
  .plan-tab {
    position: absolute; top: 163px; height: 45px; color: var(--white);
    font-size: 18px; letter-spacing: 3px; text-align: center; line-height: 46px;
  }
  .plan-tab--basic { left: 509px; width: 198px; background: var(--basic); border-radius: 40px 6px 0 0; }
  .plan-tab--pro { left: 714px; width: 196px; background: var(--pro); border-radius: 6px 6px 0 0; }
  .plan-tab--enterprise { left: 917px; width: 193px; background: var(--enterprise); border-radius: 6px 40px 0 0; }
  .plan-column {
    position: absolute; top: 213px; height: 268px; background: var(--white);
  }
  .plan-footer { position: absolute; top: 486px; height: 23px; border-radius: 0 0 4px 4px; }
  .cell {
    position: absolute; left: 0; right: 0; text-align: center;
    font-size: 17.5px; color: var(--ink); letter-spacing: 0.8px;
  }
  .cell-rule { position: absolute; left: 10px; right: 14px; height: 1px; background: var(--ink); }
  .stepper { position: absolute; width: 32px; height: 32px; }
  .stepper--minus { left: 6px; }
  .stepper--plus { right: 6px; }
  .total-bar {
    position: absolute; left: 276px; top: 553px; width: 834px; height: 55px;
    background: var(--white); border-radius: 6px;
    font-size: 35px; color: var(--ink); line-height: 55px; padding-left: 29px; letter-spacing: 1.3px;
    white-space: nowrap;
  }
</style>
</head>
<body>
  <div class="calculator-panel"></div>

  <div class="term-slider">
    <div class="term-slider__title">TERM (YRS)</div>
    <svg width="116" height="473" viewBox="0 0 116 473">
      <g stroke="var(--tick)" stroke-width="2">
        <line x1="26" y1="84" x2="86" y2="84"/><line x1="26" y1="120" x2="86" y2="120"/>
        <line x1="26" y1="156" x2="86" y2="156"/><line x1="26" y1="192" x2="86" y2="192"/>
        <line x1="26" y1="228" x2="86" y2="228"/><line x1="26" y1="264" x2="86" y2="264"/>
        <line x1="26" y1="300" x2="86" y2="300"/><line x1="26" y1="336" x2="86" y2="336"/>
        <line x1="26" y1="372" x2="86" y2="372"/><line x1="26" y1="408" x2="86" y2="408"/>
      </g>
      <rect x="47" y="77" width="18" height="359" rx="9" fill="#f3f3f3" stroke="#b5b5b5"/>
      <rect x="51" y="300" width="10" height="132" rx="5" fill="var(--mercury)"/>
      <circle cx="56" cy="302" r="24" fill="#3a3a3a"/>
      <circle cx="56" cy="302" r="20" fill="#6a6a6a"/>
      <path d="M49 308 L56 298 L63 308" fill="none" stroke="#d0d0d0" stroke-width="2"/>
    </svg>
  </div>

  <div class="field-label" style="top:236px">Clients per month:</div>
  <div class="label-rule" style="top:284px"></div>
  <div class="field-label" style="top:302px">You Cost:</div>
  <div class="label-rule" style="top:348px"></div>
  <div class="field-label" style="top:375px">Your client pays:</div>
  <div class="label-rule" style="top:426px"></div>
  <div class="field-label" style="top:452px">Monthly profit (year 4):</div>

  <div class="plan-tab plan-tab--basic">BASIC</div>
  <div class="plan-tab plan-tab--pro">PRO</div>
  <div class="plan-tab plan-tab--enterprise">ENTERPRISE</div>

  <svg width="0" height="0" style="position:absolute">
    <defs>
      <g id="minus-btn"><circle cx="16" cy="16" r="16" fill="#111"/><rect x="11" y="15" width="10" height="2" fill="#fff"/></g>
      <g id="plus-btn"><circle cx="16" cy="16" r="16" fill="#111"/><rect x="7" y="15" width="18" height="2.4" fill="#fff"/><rect x="14.8" y="7" width="2.4" height="18" fill="#fff"/></g>
    </defs>
  </svg>

  <div class="plan-column" style="left:509px;width:198px">
    <svg class="stepper stepper--minus" style="top:16px"><use href="#minus-btn"/></svg>
    <div class="cell" style="top:22px">1</div>
    <svg class="stepper stepper--plus" style="top:16px"><use href="#plus-btn"/></svg>
    <div class="cell-rule" style="top:69px"></div>
    <div class="cell" style="top:86px">$197</div>
    <div class="cell-rule" style="top:133px"></div>
    <svg class="stepper stepper--minus" style="top:156px"><use href="#minus-btn"/></svg>
    <div class="cell" style="top:160px">$297</div>
    <svg class="stepper stepper--plus" style="top:156px"><use href="#plus-btn"/></svg>
    <div class="cell-rule" style="top:211px"></div>
    <div class="cell" style="top:238px">$4,800</div>
  </div>
  <div class="plan-footer" style="left:509px;width:198px;background:var(--basic)"></div>

  <div class="plan-column" style="left:714px;width:196px">
    <svg class="stepper stepper--minus" style="top:16px"><use href="#minus-btn"/></svg>
    <div class="cell" style="top:22px">3</div>
    <svg class="stepper stepper--plus" style="top:16px"><use href="#plus-btn"/></svg>
    <div class="cell-rule" style="top:69px"></div>
    <div class="cell" style="top:86px">$297</div>
    <div class="cell-rule" style="top:133px"></div>
    <svg class="stepper stepper--minus" style="top:156px"><use href="#minus-btn"/></svg>
    <div class="cell" style="top:160px">$347</div>
    <svg class="stepper stepper--plus" style="top:156px"><use href="#plus-btn"/></svg>
    <div class="cell-rule" style="top:211px"></div>
    <div class="cell" style="top:238px">$7,200</div>
  </div>
  <div class="plan-footer" style="left:714px;width:196px;background:var(--pro)"></div>

  <div class="plan-column" style="left:917px;width:193px">
    <svg class="stepper stepper--minus" style="top:16px"><use href="#minus-btn"/></svg>
    <div class="cell" style="top:22px">2</div>
    <svg class="stepper stepper--plus" style="top:16px"><use href="#plus-btn"/></svg>
    <div class="cell-rule" style="top:69px"></div>
    <div class="cell" style="top:86px">$2500</div>
    <div class="cell-rule" style="top:133px"></div>
    <svg class="stepper stepper--minus" style="top:156px"><use href="#minus-btn"/></svg>
    <div class="cell" style="top:160px">$4000</div>
    <svg class="stepper stepper--plus" style="top:156px"><use href="#plus-btn"/></svg>
    <div class="cell-rule" style="top:211px"></div>
    <div class="cell" style="top:238px">144,000</div>
  </div>
  <div class="plan-footer" style="left:917px;width:193px;background:var(--enterprise)"></div>

  <div class="total-bar">Monthly profit by the end of year 4: $156,000</div>
</body>
</html>
```